hotel renovation business brochure 1 page front and back

Our current brochure is dated. It has too much information hence the key messages are getting lost. Key messages: one stop shopping or turn key services for hotel renovations; cheaper and quicker to renovate. The only art work that cant be changes is the logo. Using the material in the brochure, create a more concise message to clients while still informing them of all the services we do. Need to update color scheme to match the logo. Would like to have a few examples of renovation we have done and possibly a listing of hotel brands we have worked on.

Target Market(s)

Hotel management companies, hotel investment companies, hotel owners

Industry/Entity Type

Hospitality

Requirements
Must have
• -1 page front and back
• -be able to communicate message as one stop shopping for hotel renovations, cheaper and faster
• - bellmoor works logo design must remain
• - consistent color palette that matches logo
• - hotel brands we have worked with
• -contact information
• -pictures of renovations. can use what is in brochure or other photos attached.
Should not have
• -too many words like in current brochure but needs to communicate our advantage and all the services we offer
• -

```html
<!DOCTYPE html>
<html lang="en">
<head>
<meta charset="utf-8">
<title>bellmoor works — Renovation Brochure</title>
<link href="https://fonts.googleapis.com/css2?family=Source+Sans+3:ital,wght@0,400;0,600;0,700;1,400&display=swap" rel="stylesheet">
<style>
  :root{
    --navy:#2b3947;
    --brand-blue:#2f4f8f;
    --ink:#3a3d42;
    --panel-grey:#e4e5e7;
    --paper:#ffffff;
    --backdrop:#d9d7d3;
  }
  *{margin:0;padding:0;box-sizing:border-box}
  html,body{width:1200px;height:814px;overflow:hidden;background:var(--backdrop)}
  body{position:relative;font-family:"Source Sans 3",Arial,sans-serif;color:var(--ink)}
  .page{position:absolute;width:483px;height:622px;background:var(--paper);box-shadow:0 2px 6px rgba(0,0,0,.18);overflow:hidden}
  .page--front{left:96px;top:93px}
  .page--back{left:615px;top:96px}
  .page__art{position:absolute;inset:0;width:100%;height:100%}
  .abs{position:absolute}

  /* front */
  .brand{left:14px;top:40px;display:flex;align-items:center;gap:7px}
  .brand__mark{width:22px;height:22px;background:var(--brand-blue)}
  .brand__name{font-size:19px;font-weight:700;color:var(--navy);line-height:1}
  .brand__city{left:14px;top:72px;font-size:13px;font-weight:700;letter-spacing:4px;color:var(--brand-blue)}
  .services{display:flex;gap:22px;color:#fff;font-size:10.5px;line-height:14px;list-style:none}
  .services ul{list-style:none}
  .services li{position:relative;padding-left:12px}
  .services li::before{content:"";position:absolute;left:0;top:4px;width:6px;height:6px;border-radius:50%;background:#fff}
  .callout{color:#fff;text-align:center;text-transform:uppercase;font-size:11.5px;line-height:16.5px}
  .section-title{font-size:12.5px;font-weight:600;color:var(--brand-blue);text-transform:uppercase;line-height:1}
  .body-copy{font-size:8.8px;line-height:10.8px;text-align:justify}
  .highlight{font-size:7.4px;line-height:10.6px;font-weight:600;color:var(--brand-blue);text-transform:uppercase;text-align:justify}
  .contact{text-align:right;font-size:11px;line-height:14.5px}
  .contact__web{font-size:12px;font-weight:600;color:var(--brand-blue)}

  /* back */
  .quote{color:#fff;font-style:italic;font-size:9px;line-height:12.5px;text-align:center}
  .benefit .section-title{font-size:11.5px;margin-bottom:1px}
  .benefit .body-copy{font-size:8.4px;line-height:10.2px}
</style>
</head>
<body>

<section class="page page--front">
  <svg class="page__art" viewBox="0 0 604 781" preserveAspectRatio="none" aria-hidden="false">
    <defs>
      <linearGradient id="lobbyTone" x1="0" y1="0" x2="1" y2="1"><stop offset="0" stop-color="#c9a56a"/><stop offset=".5" stop-color="#8b6a4c"/><stop offset="1" stop-color="#b8a48c"/></linearGradient>
      <linearGradient id="roomTone" x1="0" y1="0" x2="1" y2="1"><stop offset="0" stop-color="#8a4a2c"/><stop offset=".6" stop-color="#d9d3c8"/><stop offset="1" stop-color="#6e5a4a"/></linearGradient>
      <linearGradient id="loungeTone" x1="0" y1="0" x2="1" y2="1"><stop offset="0" stop-color="#6e4a2e"/><stop offset=".5" stop-color="#c89a4a"/><stop offset="1" stop-color="#d8c48a"/></linearGradient>
      <linearGradient id="suiteTone" x1="0" y1="0" x2="1" y2="1"><stop offset="0" stop-color="#3a2e28"/><stop offset=".5" stop-color="#c4b49a"/><stop offset="1" stop-color="#5a4a3e"/></linearGradient>
    </defs>
    <polygon points="0,160 162,160 42,480 0,480" fill="var(--panel-grey)"/>
    <polygon points="210,14 604,14 604,355 94,355" fill="url(#lobbyTone)" role="img" aria-label="Renovated hotel lobby with stone fireplace, sofas and chandelier"/>
    <polygon points="82,365 460,365 425,468 45,468" fill="var(--navy)"/>
    <polygon points="470,365 604,365 604,468 437,468" fill="url(#roomTone)" role="img" aria-label="Renovated guest room with king bed"/>
    <polygon points="40,478 222,478 200,582 20,582" fill="url(#loungeTone)" role="img" aria-label="Hotel lounge seating by a stone fireplace"/>
    <polygon points="240,478 418,478 392,582 208,582" fill="url(#suiteTone)" role="img" aria-label="Guest room with two beds"/>
    <polygon points="428,478 604,478 604,582 393,582" fill="var(--navy)"/>
    <polygon points="390,592 604,592 604,781 320,781" fill="var(--panel-grey)"/>
  </svg>

  <div class="abs brand"><span class="brand__mark"></span><span class="brand__name">bellmoor works</span></div>
  <div class="abs brand__city">ASHFORD</div>

  <div class="abs services" style="left:86px;top:307px">
    <ul><li>Planning</li><li>Design</li><li>Specification</li><li>FF&amp;E</li></ul>
    <ul><li>Logistics</li><li>Construction</li><li>Installation</li><li>Warranty Administration</li></ul>
  </div>

  <p class="abs callout" style="left:336px;top:401px;width:147px">A complete<br>renovation with<br>just one call!</p>

  <h2 class="abs section-title" style="left:14px;top:493px">Turn-Key Renovations</h2>
  <p class="abs body-copy" style="left:14px;top:518px;width:265px">If you want to sell more rooms and generate better guest reviews, you need bellmoor works to keep you fresh and up to date. We combine top designers, complete FF&amp;E, turn key construction and installation into a single affordable package.</p>
  <p class="abs highlight" style="left:14px;top:578px;width:246px">If you're fulfilling a PIP, upgrading, or expanding a resort or timeshare, you'll save money and achieve more success with bellmoor works.</p>

  <div class="abs contact" style="right:9px;top:552px">
    <p>bellmoor works</p>
    <p>Ashford, NC</p>
    <p>555-014-2287 / 555-019-6630</p>
    <p class="contact__web">www.bellmoorworks.com</p>
  </div>
</section>

<section class="page page--back">
  <svg class="page__art" viewBox="0 0 604 781" preserveAspectRatio="none">
    <defs>
      <linearGradient id="patioTone" x1="0" y1="0" x2="0" y2="1"><stop offset="0" stop-color="#c9b89a"/><stop offset=".5" stop-color="#6a5a4a"/><stop offset="1" stop-color="#9a9488"/></linearGradient>
      <linearGradient id="kingTone" x1="0" y1="0" x2="1" y2="1"><stop offset="0" stop-color="#2a2f4a"/><stop offset=".5" stop-color="#c8a050"/><stop offset="1" stop-color="#e0d8c8"/></linearGradient>
      <linearGradient id="modernTone" x1="0" y1="0" x2="1" y2="1"><stop offset="0" stop-color="#e8e8e8"/><stop offset=".6" stop-color="#6a6a6e"/><stop offset="1" stop-color="#2e2e34"/></linearGradient>
      <linearGradient id="deskTone" x1="0" y1="0" x2="1" y2="1"><stop offset="0" stop-color="#7a5a3e"/><stop offset=".6" stop-color="#3a3a40"/><stop offset="1" stop-color="#2a4a9a"/></linearGradient>
    </defs>
    <polygon points="0,12 604,12 604,238 0,238" fill="url(#patioTone)" role="img" aria-label="Hotel courtyard patio with stone fire pit and lounge chairs"/>
    <polygon points="0,250 457,250 430,354 0,354" fill="var(--navy)"/>
    <polygon points="467,250 604,250 604,354 438,354" fill="url(#kingTone)" role="img" aria-label="Guest room with king bed and gold bedding"/>
    <polygon points="0,364 228,364 205,468 0,468" fill="url(#modernTone)" role="img" aria-label="Modern guest room with white bedding"/>
    <polygon points="238,364 420,364 395,468 212,468" fill="url(#deskTone)" role="img" aria-label="Guest room with wood wall and work desk"/>
    <polygon points="430,364 604,364 604,468 395,468" fill="var(--navy)"/>
    <rect x="0" y="670" width="604" height="111" fill="var(--panel-grey)"/>
    <g aria-label="Hotel brands we have worked with" role="img">
      <rect x="20" y="694" width="22" height="24" fill="#2f7a6a"/>
      <rect x="48" y="698" width="64" height="16" fill="#b8324a"/>
      <rect x="120" y="692" width="74" height="26" fill="#2a2a2a"/>
      <rect x="200" y="692" width="30" height="26" fill="#6a8a5a"/>
      <rect x="238" y="692" width="42" height="28" fill="#1c3a6a"/>
      <rect x="286" y="692" width="56" height="28" fill="#2a8a4a"/>
      <circle cx="364" cy="706" r="14" fill="#1f5a3a"/>
      <rect x="386" y="693" width="46" height="26" rx="8" fill="#2a3a8a"/>
      <rect x="442" y="692" width="36" height="28" fill="#c8202a"/>
      <rect x="488" y="698" width="38" height="18" fill="#1c4a9a"/>
      <rect x="532" y="700" width="54" height="12" fill="#b82a2a"/>
      <rect x="18" y="734" width="58" height="26" fill="#2a2a2a"/>
      <circle cx="90" cy="746" r="12" fill="#2a4a9a"/>
      <rect x="106" y="734" width="36" height="26" fill="#5a1a2a"/>
      <rect x="148" y="734" width="26" height="26" fill="#7a1a2a"/>
      <rect x="178" y="736" width="92" height="22" fill="#1a3a7a"/>
      <rect x="276" y="734" width="42" height="26" fill="#2a7a6a"/>
      <rect x="322" y="734" width="46" height="26" fill="#1a4a9a"/>
      <rect x="372" y="736" width="58" height="22" fill="#3a4a6a"/>
      <rect x="436" y="734" width="40" height="26" fill="#2a4a9a"/>
      <rect x="482" y="734" width="52" height="26" fill="#6a9a2a"/>
      <rect x="540" y="738" width="36" height="18" fill="#8a2a2a"/>
      <circle cx="590" cy="746" r="8" fill="#d8a030"/>
    </g>
  </svg>

  <p class="abs quote" style="left:16px;top:225px;width:312px">“To maximize your property's value, you must continually provide fresh style and quality. I founded bellmoor works in 1998 to take your property to new heights with less cost - and no hassle.” - Marian Holt</p>
  <p class="abs callout" style="left:316px;top:316px;width:167px">100% custom<br>and complete!</p>

  <div class="abs benefit" style="left:15px;top:388px;width:460px">
    <h2 class="section-title">Industry Leading Design</h2>
    <p class="body-copy" style="text-align:left">bellmoor works' experienced NDCA designers are the best in the industry – but our fees are LOW! If you are a franchise, we'll prepare all design submittals and guide you through all approvals. If you're independent, we'll give you exciting features that meet your exact needs and attract more guests.</p>
  </div>
  <div class="abs benefit" style="left:15px;top:440px;width:222px">
    <h2 class="section-title">Save Money</h2>
    <p class="body-copy">Buy at industry's best prices. Deal with just one vendor and get domestic and international buying power on everything.</p>
  </div>
  <div class="abs benefit" style="left:251px;top:440px;width:222px">
    <h2 class="section-title">Save Stress</h2>
    <p class="body-copy" style="text-align:left">We manage every detail for you. There is no renovation problem we can't solve.</p>
  </div>
  <div class="abs benefit" style="left:15px;top:491px;width:222px">
    <h2 class="section-title">Save Time</h2>
    <p class="body-copy">We coordinate all design, purchasing, construction and installation so your entire renovation will go faster.</p>
  </div>
  <div class="abs benefit" style="left:251px;top:491px;width:222px">
    <h2 class="section-title">Get Better Results</h2>
    <p class="body-copy" style="text-align:left">Your project will integrate and look better from start to finish.</p>
  </div>
</section>

</body>
</html>
```